Blue Quill - tailored CVs templates

Wanting 6 -8 C.V templates that are professional and can be used to sent to a human resource manager. The market base is wide so generic is best to cover all areas however a couple of designer templates would be great. The main type of customers requiring CVs are business oriented however there is retail, construction, health and all the key arers of employment.

Target Market(s)

Anyone applying for a job to human resource department

Industry/Entity Type

Business

Colors

Designer to choose colors to be used in the design.

Requirements
Must have
• a good layout, easy to read format, must be able to write details on for cusomters eg work experince etc.
Nice to have
• looking for a range of 6 - 8 differnet templates, majority geneic and couple desiger templates

```html
<!DOCTYPE html>
<html lang="en">
<head>
<meta charset="utf-8">
<title>Hot Shot — Resume</title>
<link href="https://fonts.googleapis.com/css2?family=Lato:wght@400;700;900&display=swap" rel="stylesheet">
<style>
:root{
  --backdrop:#e4e5e7;
  --paper:#ffffff;
  --sidebar:#2d3d4f;
  --ink:#2a3646;
  --muted:#9a9ea3;
  --rule:#b9bcc0;
  --dot-off:#a5a8ac;
  --map:#d5d7da;
  --on-dark:#ffffff;
}
*{box-sizing:border-box;margin:0;padding:0}
html,body{width:1193px;height:1200px;overflow:hidden;background:var(--backdrop);font-family:'Lato',sans-serif;color:var(--ink)}
.resume{position:absolute;left:154px;top:20px;width:885px;height:1161px;background:var(--paper);box-shadow:0 4px 14px rgba(0,0,0,.12)}
.resume *{position:absolute}
.resume section{position:static}
.sidebar{left:0;top:0;width:257px;height:1161px;background:var(--sidebar);color:var(--on-dark)}
.portrait{left:28px;top:32px;width:202px;height:202px;border-radius:50%;border:4px solid #fff;background:radial-gradient(circle at 50% 40%,#c9c7c4,#7d7a78)}
.side-heading{left:42px;font-size:19px;letter-spacing:3.5px;font-weight:400;line-height:1;white-space:nowrap}
.side-rule{left:42px;width:169px;height:1.5px;background:#d9dde2}
.side-text{left:42px;width:172px;font-size:12.5px;line-height:17.5px;color:#e6e9ec}
.contact{left:42px;width:180px;height:24px;font-size:11px;line-height:13px;color:#e6e9ec}
.contact svg{position:absolute;left:0;top:0}
.contact span{left:46px;top:5px;width:150px;white-space:nowrap}
.contact.two span{top:0}

.eyebrow{left:308px;top:70px;font-size:18px;font-weight:700;color:#444b54;white-space:nowrap}
.name{left:306px;top:90px;font-size:43px;font-weight:700;letter-spacing:2px;line-height:1;color:var(--ink);white-space:nowrap}
.role{left:308px;top:141px;font-size:18px;letter-spacing:1px;color:#8c9096;white-space:nowrap}
.map{left:621px;top:40px;width:243px;height:190px;border-radius:40px 60px 30px 50px;background:radial-gradient(ellipse at 50% 40%,#cfd1d4,#e6e7e9)}
.main-heading{left:308px;font-size:20px;letter-spacing:4px;font-weight:700;color:#3a4656;line-height:1;white-space:nowrap}
.main-rule{left:308px;width:534px;height:2px;background:var(--rule)}

.company{left:308px;font-size:12.5px;font-weight:700;color:var(--ink);line-height:1;white-space:nowrap}
.company i{position:static;font-weight:400;font-size:10px;margin-left:8px}
.company-rule{height:1.5px;background:var(--rule)}
.position{left:308px;font-size:20px;font-weight:900;line-height:1;color:var(--ink);white-space:nowrap}
.rating{left:474px;width:124px;height:14px}
.years{left:690px;font-size:13px;font-weight:700;line-height:1;white-space:nowrap}
.blurb{left:308px;width:534px;font-size:10.8px;line-height:17px;color:var(--muted);text-align:justify}

.school{font-size:13px;font-weight:900;line-height:1;white-space:nowrap}
.place{font-size:10px;font-style:italic;line-height:1;color:#555;white-space:nowrap}
.school-text{width:220px;font-size:10.5px;line-height:19.5px;color:#444}

.skill-icons{left:630px;top:913px;width:212px;height:24px}
.skill-title{left:308px;top:977px;font-size:19px;color:#3a4656;line-height:1;font-weight:400;white-space:nowrap}
.skill-list{left:308px;top:1019px;width:300px;list-style:none}
.skill-list li{position:relative;padding-left:22px;font-size:12px;line-height:19.5px;color:var(--muted);white-space:nowrap}
.skill-list li::before{content:"";position:absolute;left:1px;top:5px;width:11px;height:11px;border-radius:50%;background:#6b7078}
.meter-label{left:704px;font-size:12px;font-weight:900;line-height:1;white-space:nowrap}
.meter{left:704px;width:138px;height:9px;background:#8f9398}
.meter b{left:0;top:0;height:9px;background:#3d4651}
</style>
</head>
<body>
<main class="resume">
  <aside class="sidebar">
    <div class="portrait" role="img" aria-label="Portrait photo of the candidate"></div>

    <h2 class="side-heading" style="top:274px">PROFILE</h2>
    <div class="side-rule" style="top:306px"></div>
    <p class="side-text" style="top:338px">Lorem ipsum dolor sit amet, consectetur adipiscing elit. Nulla lorem ectus, tempus id fringilla ut, molestie ac nibh. Integer ornare, diam in molestie m, felis libero itudin est, porttitor egestas enim libero sit amet massa. Donec porttitor dolor et</p>

    <h2 class="side-heading" style="top:565px">CONTACTS</h2>
    <div class="side-rule" style="top:594px"></div>
    <div class="contact" style="top:624px">
      <svg width="24" height="24" viewBox="0 0 24 24"><circle cx="12" cy="12" r="10.5" fill="none" stroke="#fff" stroke-width="1.5"/><path d="M7 10c0-2 10-2 10 0l-1 1.5h-2l-.5-1h-3l-.5 1H8zM8.5 12h7l1 4h-9z" fill="#fff"/></svg>
      <span>000 . 555 . 0147</span>
    </div>
    <div class="contact" style="top:652px">
      <svg width="24" height="24" viewBox="0 0 24 24"><circle cx="12" cy="12" r="10.5" fill="none" stroke="#fff" stroke-width="1.5"/><rect x="6.5" y="8" width="11" height="8" rx="1" fill="#fff"/><path d="M6.5 8.5l5.5 4 5.5-4" fill="none" stroke="#2d3d4f" stroke-width="1.2"/></svg>
      <span>hello@bluequill.com</span>
    </div>
    <div class="contact" style="top:680px">
      <svg width="24" height="24" viewBox="0 0 24 24"><circle cx="12" cy="12" r="10.5" fill="none" stroke="#fff" stroke-width="1.5"/><circle cx="12" cy="12" r="5.5" fill="none" stroke="#fff" stroke-width="1.3"/><path d="M6.5 12h11M12 6.5c-3 3-3 8 0 11M12 6.5c3 3 3 8 0 11" fill="none" stroke="#fff" stroke-width="1"/></svg>
      <span>bluequillcv.com</span>
    </div>
    <div class="contact two" style="top:706px">
      <svg width="24" height="24" viewBox="0 0 24 24"><circle cx="12" cy="12" r="10.5" fill="none" stroke="#fff" stroke-width="1.5"/><path d="M6 12l6-5.5 6 5.5h-1.8v5h-8.4v-5z" fill="#fff"/><rect x="10.8" y="13.5" width="2.4" height="3.5" fill="#2d3d4f"/></svg>
      <span>12 Quill Lane<br>Harbor City, HC 40210</span>
    </div>

    <h2 class="side-heading" style="top:785px">REFERENCES</h2>
    <div class="side-rule" style="top:814px"></div>
    <p class="side-text" style="top:836px">Lorem ipsum dolor sit amet, consectetur adipiscing elit. Nulla lorem ectus, tempus id fringilla ut, molestie ac nibh.</p>

    <h2 class="side-heading" style="top:976px;letter-spacing:.5px">Position</h2>
    <div class="side-rule" style="top:1008px"></div>
    <p class="side-text" style="top:1016px">Lorem ipsum dolor sit amet, consectetur adipiscing elit. Nulla lorem ectus, tempus id fringilla ut, molestie ac nibh.</p>
  </aside>

  <div class="map" role="img" aria-label="World map with location markers"></div>

  <p class="eyebrow">Resume</p>
  <h1 class="name">HOT SHOT</h1>
  <p class="role">Web &amp; App Designer</p>

  <h2 class="main-heading" style="top:213px">WORK EXPERIENCE</h2>
  <div class="main-rule" style="top:251px"></div>

  <section class="job">
    <p class="company" style="top:274px">Company Name<i>city, state, country</i></p>
    <div class="company-rule" style="left:528px;width:314px;top:282px"></div>
    <h3 class="position" style="top:293px">Current Position</h3>
    <svg class="rating" style="top:296px" viewBox="0 0 124 14"><g fill="#2a3646"><circle cx="7" cy="7" r="6.3"/><circle cx="29" cy="7" r="6.3"/><circle cx="51" cy="7" r="6.3"/></g><g fill="#a5a8ac"><circle cx="73" cy="7" r="6.3"/><circle cx="95" cy="7" r="6.3"/><circle cx="117" cy="7" r="6.3"/></g></svg>
    <p class="years" style="top:297px">2010-2016</p>
    <p class="blurb" style="top:323px">Lorem ipsum dolor sit amet, consectetur adipiscing elit. Nulla lorem ectus, tempus id fringilla ut, molestie ac nibh. Integer ornare, diam in molestie m, felis libero itudin est, porttitor egestas enim libero sit amet massa. Donec porttitor dolor et nisl convallis felis libero itudin est, porttitor egestas enim libero sit amet massa.</p>
  </section>

  <section class="job">
    <p class="company" style="top:440px">Company Name<i>city, state, country</i></p>
    <div class="company-rule" style="left:528px;width:260px;top:448px"></div>
    <h3 class="position" style="top:459px">Current Position</h3>
    <svg class="rating" style="top:462px" viewBox="0 0 124 14"><g fill="#2a3646"><circle cx="7" cy="7" r="6.3"/><circle cx="29" cy="7" r="6.3"/><circle cx="51" cy="7" r="6.3"/></g><g fill="#a5a8ac"><circle cx="73" cy="7" r="6.3"/><circle cx="95" cy="7" r="6.3"/><circle cx="117" cy="7" r="6.3"/></g></svg>
    <p class="years" style="top:463px">2010-2016</p>
    <p class="blurb" style="top:488px">Lorem ipsum dolor sit amet, consectetur adipiscing elit. Nulla lorem ectus, tempus id fringilla ut, molestie ac nibh. Integer ornare, diam in molestie m, felis libero itudin est, porttitor egestas enim libero sit amet massa. Donec porttitor dolor et nisl convallis felis libero itudin est, porttitor egestas enim libero sit amet massa.</p>
  </section>

  <section class="job">
    <p class="company" style="top:598px">Company Name<i>city, state, country</i></p>
    <div class="company-rule" style="left:528px;width:314px;top:606px"></div>
    <h3 class="position" style="top:617px">Current Position</h3>
    <svg class="rating" style="top:620px" viewBox="0 0 124 14"><g fill="#2a3646"><circle cx="7" cy="7" r="6.3"/><circle cx="29" cy="7" r="6.3"/><circle cx="51" cy="7" r="6.3"/></g><g fill="#a5a8ac"><circle cx="73" cy="7" r="6.3"/><circle cx="95" cy="7" r="6.3"/><circle cx="117" cy="7" r="6.3"/></g></svg>
    <p class="years" style="top:621px">2010-2016</p>
    <p class="blurb" style="top:646px">Lorem ipsum dolor sit amet, consectetur adipiscing elit. Nulla lorem ectus, tempus id fringilla ut, molestie ac nibh. Integer ornare, diam in molestie m, felis libero itudin est, porttitor egestas enim libero sit amet massa. Donec porttitor dolor et nisl convallis felis libero itudin est, porttitor egestas enim libero sit amet massa.</p>
  </section>

  <h2 class="main-heading" style="top:741px">EDUCATION</h2>
  <div class="main-rule" style="top:777px"></div>

  <section class="school-block">
    <h3 class="school" style="left:308px;top:799px">Praesent laoreet College</h3>
    <p class="place" style="left:308px;top:814px">Curabitur&nbsp; New York</p>
    <p class="school-text" style="left:308px;top:826px">Lorem ipsum dolor sit amet, consectetur adipiscing elit. Nulla ectusinut,consectetur adipiscing elit.</p>
  </section>
  <section class="school-block">
    <h3 class="school" style="left:626px;top:799px">Praesent laoreet School</h3>
    <p class="place" style="left:626px;top:814px">Curabitur&nbsp; New York</p>
    <p class="school-text" style="left:626px;top:826px">Lorem ipsum dolor sit amet, consectetur adipiscing elit. Nulla ectusinut,consectetur adipiscing elit.</p>
  </section>

  <h2 class="main-heading" style="top:917px">SKILLS</h2>
  <svg class="skill-icons" viewBox="0 0 212 24" fill="none" stroke="#3a4656" stroke-width="1.6">
    <rect x="2" y="6" width="18" height="13" rx="1.5"/><path d="M20 10l7-4v13l-7-4"/><circle cx="9" cy="12.5" r="2.5"/>
    <rect x="73" y="4" width="18" height="12" rx="1"/><path d="M69 19h26"/>
    <path d="M135 9h14c3 0 5 9 3 11-1.5 1.5-4-1-6-3h-8c-2 2-4.5 4.5-6 3-2-2 0-11 3-11z"/><path d="M138 12v4M136 14h4"/><circle cx="146" cy="13" r=".8"/><circle cx="148" cy="15" r=".8"/>
    <rect x="191" y="3" width="16" height="14" rx="1"/><path d="M188 20h20l-2-3"/>
  </svg>
  <div class="main-rule" style="top:952px"></div>

  <h3 class="skill-title">Current Position</h3>
  <ul class="skill-list">
    <li>Design East Pixel Bld. 99 Creative City 9000</li>
    <li>Design East Pixel Bld. 99 Creative City 9000</li>
    <li>Design East Pixel Bld. 99 Creative City 9000</li>
    <li>Design East Pixel Bld. 99 Creative City 9000</li>
    <li>Design East Pixel Bld. 99 Creative City 9000</li>
  </ul>

  <p class="meter-label" style="top:1001px">East Pixel Bld. 99</p>
  <div class="meter" style="top:1021px"><b style="width:92px"></b></div>
  <p class="meter-label" style="top:1038px">Creative City 9000</p>
  <div class="meter" style="top:1058px"><b style="width:60px"></b></div>
  <p class="meter-label" style="top:1075px">Republic of Design</p>
  <div class="meter" style="top:1095px"><b style="width:138px"></b></div>
</main>
</body>
</html>
```